redesing professional certificate

Redesign our certificate to more a professional look and to make it look like a-wanna have - Best in adobe photoshop, because this template will be our basic, and we have in our education different levels, basic, upper, lower, complex, master level. I usually add a small picture to show what level they are. Or when you have a better suggestion I a gladly to hear.
We teach to physiotherapist so it has to look professional.

Target Market(s)

physiotherapist

Industry/Entity Type

Health Care

Requirements
Must have
• our logo

```html
<!DOCTYPE html>
<html lang="en">
<head>
<meta charset="utf-8">
<title>Certificate – Master Level</title>
<link href="https://fonts.googleapis.com/css2?family=Montserrat:ital,wght@0,400;0,600;0,700;1,400&family=Philosopher:wght@700&display=swap" rel="stylesheet">
<style>
  :root {
    --backdrop: #000000;
    --paper: #ffffff;
    --level-yellow: #f8c824;
    --level-yellow-light: #fbd85a;
    --ink: #14213a;
    --ink-soft: #3a4558;
  }
  * { margin: 0; padding: 0; box-sizing: border-box; }
  html, body {
    width: 1200px; height: 1200px; overflow: hidden;
    background: var(--backdrop);
  }
  .stage {
    width: 1200px; height: 1200px;
    display: flex; align-items: center; justify-content: center;
  }
  .certificate {
    position: relative;
    width: 790px; height: 1100px;
    background: var(--paper);
    color: var(--ink);
    font-family: "Montserrat", sans-serif;
    box-shadow: 0 10px 40px rgba(0,0,0,.5);
  }
  .level-band {
    position: absolute; left: 0; right: 0;
    background: linear-gradient(100deg, var(--level-yellow), var(--level-yellow-light) 50%, var(--level-yellow));
  }
  .level-band--top {
    top: 24px; height: 110px;
    display: flex; align-items: center; justify-content: center;
  }
  .level-band--bottom { bottom: 0; height: 40px; }
  .level-band__title {
    color: var(--paper);
    font-weight: 700; font-size: 34px; letter-spacing: 1px;
  }
  .brand {
    position: absolute; top: 190px; left: 0; right: 0;
    display: flex; align-items: center; justify-content: center; gap: 14px;
  }
  .brand__dot {
    width: 40px; height: 40px; border-radius: 50%;
    background: var(--ink);
  }
  .brand__name {
    font-weight: 700; font-size: 34px; color: var(--ink);
  }
  .recipient {
    position: absolute; top: 300px; left: 0; right: 0;
    text-align: center;
  }
  .recipient__name {
    font-family: "Philosopher", serif;
    font-weight: 700; font-size: 46px;
  }
  .recipient__lead {
    margin-top: 18px; font-size: 19px; color: var(--ink-soft);
  }
  .course {
    margin-top: 14px; font-size: 20px; line-height: 1.5;
  }
  .course__title { font-weight: 700; }
  .signatures {
    position: absolute; top: 580px; left: 100px; right: 110px; height: 110px;
    font-style: italic; font-size: 19px; line-height: 1.6;
  }
  .signatures__person { position: absolute; }
  .signatures__person--left { left: 0; top: 0; }
  .signatures__person--right { right: 0; top: 50px; }
  .details {
    position: absolute; top: 720px; left: 90px; right: 90px;
    font-size: 19px; line-height: 1.4;
  }
  .details__registration { font-weight: 600; }
  .details__terms { margin-top: 14px; font-weight: 600; }
  .issuer { margin-top: 26px; font-weight: 600; font-style: normal; line-height: 1.35; }
  .tagline { margin-top: 26px; font-weight: 600; }
</style>
</head>
<body>
<main class="stage">
  <article class="certificate">
    <header class="level-band level-band--top">
      <h1 class="level-band__title">Certificate</h1>
    </header>

    <div class="brand">
      <span class="brand__dot"></span>
      <span class="brand__name">Myolinea</span>
    </div>

    <section class="recipient">
      <h2 class="recipient__name">Physiotherapist Name</h2>
      <p class="recipient__lead">has completed</p>
      <p class="course">
        <span class="course__title">The Fasciatherapy Master Level Course</span><br>
        3 days, 15-17 April 2020<br>
        Kópavogur, Iceland 17 April 2020
      </p>
    </section>

    <section class="signatures">
      <p class="signatures__person signatures__person--left">Mr. JT v.d. Berg<br>Co-Director</p>
      <p class="signatures__person signatures__person--right">Mr. PM Hollis<br>Co-Director</p>
    </section>

    <section class="details">
      <p class="details__registration">Registration Number: 1 ICE 20</p>
      <p class="details__terms">The Myolinea Practitioner Programme ongoing certification is contingent upon meeting the requirements of the maintenanace of the certification of faschiatherapy.</p>
      <address class="issuer">
        Tissuewerk BV<br>
        Tweede Lindenkade 14<br>
        1015KL Amsterdam<br>
        The Netherlands
      </address>
      <p class="tagline">Specialist in Fasciatherapy innovation.</p>
    </section>

    <footer class="level-band level-band--bottom"></footer>
  </article>
</main>
</body>
</html>
```